Financial Planning business needs a new Business Card design

We need a business card design for an Australian financial planning business. I am looking for a clean simple design

Target Market(s)

People aged 25-40

Industry/Entity Type

Financial Service

Contact Information for Business Card

On the front of the card we need the following information:
Name: Colin Merrow (First Name Green: #006838 and last name Grey: #414042)
Position: Financial Adviser
Qualifications: BEc(Hons), AdDipFS(FP), Dip FMBM, CFL®
Mobile: 0437 512 604
Email: colin@brightledgeplan.com.au

On the back of the card we need:
Postal address: PO BOX 5307, PERTH BC, WA 6849
Website: www.brightledgeplan.com.au
Text: AFS Licence No. 518760

The fields need to be able to be edited.

Font styles to use
Sans Serif

Requirements
Must have
• Information listed above

```html
<!DOCTYPE html>
<html lang="en">
<head>
<meta charset="utf-8">
<title>Brightledge Business Card</title>
<link rel="stylesheet" href="https://fonts.googleapis.com/css2?family=Oswald:wght@600;700&family=Arimo:wght@400;700&display=swap">
<style>
  :root {
    --brand-green: #006838;
    --brand-grey: #414042;
    --card-white: #ffffff;
    --backdrop: #26272b;
    --text-light: #ffffff;
  }
  * { margin: 0; padding: 0; box-sizing: border-box; }
  html, body {
    width: 1200px;
    height: 900px;
    overflow: hidden;
    background: var(--backdrop);
  }
  .stage {
    position: relative;
    width: 1200px;
    height: 900px;
  }
  .card {
    position: absolute;
    width: 520px;
    height: 318px;
    border-radius: 4px;
    box-shadow: 0 14px 30px rgba(0, 0, 0, 0.45);
    display: flex;
    flex-direction: column;
    justify-content: center;
  }

  /* Back of card */
  .card-back {
    left: 70px;
    top: 130px;
    background: var(--brand-green);
    color: var(--text-light);
    padding-left: 70px;
  }
  .card-back .wordmark {
    font-family: "Oswald", sans-serif;
    font-weight: 700;
    font-size: 56px;
    line-height: 1;
    letter-spacing: 0.5px;
    color: var(--text-light);
    text-transform: uppercase;
  }
  .back-details {
    margin-top: 18px;
    font-family: "Arimo", sans-serif;
    font-size: 14px;
    line-height: 1.45;
  }
  .back-details .website { font-weight: 700; }

  /* Front of card */
  .card-front {
    left: 610px;
    top: 440px;
    background: var(--card-white);
    padding-left: 70px;
  }
  .card-front .wordmark {
    font-family: "Oswald", sans-serif;
    font-weight: 700;
    font-size: 56px;
    line-height: 1;
    letter-spacing: 0.5px;
    color: var(--brand-green);
    text-transform: uppercase;
  }
  .person-name {
    margin-top: 20px;
    font-family: "Oswald", sans-serif;
    font-weight: 600;
    font-size: 24px;
    line-height: 1;
    text-transform: uppercase;
  }
  .person-name .first-name { color: var(--brand-green); }
  .person-name .last-name { color: var(--brand-grey); }
  .person-role {
    margin-top: 4px;
    font-family: "Arimo", sans-serif;
    font-weight: 700;
    font-size: 14px;
    color: var(--brand-grey);
  }
  .person-qualifications {
    margin-top: 6px;
    font-family: "Arimo", sans-serif;
    font-size: 12.5px;
    color: var(--brand-grey);
  }
  .contact-list {
    margin-top: 12px;
    list-style: none;
    font-family: "Arimo", sans-serif;
    font-size: 13px;
    line-height: 1.5;
    color: var(--brand-grey);
  }
  .contact-list .label {
    color: var(--brand-green);
    font-weight: 700;
  }
</style>
</head>
<body>
  <main class="stage">
    <section class="card card-back" aria-label="Card back">
      <div class="wordmark">Brightledge</div>
      <div class="back-details">
        <p class="postal">PO BOX 5307, PERTH BC, WA 6849</p>
        <p class="website">www.brightledgeplan.com.au</p>
        <p class="licence">AFS Licence No. 518760</p>
      </div>
    </section>

    <section class="card card-front" aria-label="Card front">
      <div class="wordmark">Brightledge</div>
      <h1 class="person-name"><span class="first-name">Colin</span> <span class="last-name">Merrow</span></h1>
      <p class="person-role">Financial Adviser</p>
      <p class="person-qualifications">BEC(HONS), ADDIPFS(FP), DIP FMBM, CFL®</p>
      <ul class="contact-list">
        <li><span class="label">M:</span> 0437 512 604</li>
        <li><span class="label">E:</span> colin@brightledgeplan.com.au</li>
      </ul>
    </section>
  </main>
</body>
</html>
```